Wedding Invitation for a wedding at home - personal, romantic event

Want a wedding invitation that is to be printed onto card.
Size to be 148mm x 210mm
For it to open like a book not tent card
Have a picture of a house that I want to be the front cover.
I've attached 2 pictures. I like the picture without the man but with the grass
For the photo to become a drawing and the colours to be brighter.
If you could use the picture of us and get us in one of the windows.
If you could put the picture of the dog maybe somewhere on the grass.
Love the colour of the sky in the picture of the beach

Words to be on the inside of the card:
Together with our families
You are invited to the Wedding Reception of Polly Faraway and Ned Bramwick
On Saturday 9th of September 2017 at 6pm
At Bramwick's Keep, 41b, Fennow Crescent, Camberley, Surrey, GU19 7QX
Carriages at 1am
RSVP by Friday 27th of July to 07712 958 061

Words on the Back page:
With all that we have, we've been truly blessed.
Your presence and prayers are all that we request.
But if you desire to give nonetheless,
Monetary gift is one we suggest.

If the pages can be white.
Writing in gold
gold border on all pages

Target Market(s)

Wedding guests

Industry/Entity Type

Wedding

Font styles to use
Script

Requirements
Must have
• Romantic feel. Our wedding colours are white, gold and rose gold.
• Designer to be creative and I do not have much inspiration.
Nice to have
• metallic colours
• Maybe have MR & MRS in gold metallic on the front page

```html
<!DOCTYPE html>
<html lang="en">
<head>
<meta charset="utf-8">
<title>Polly &amp; Ned – Wedding Invitation</title>
<link rel="stylesheet" href="https://fonts.googleapis.com/css2?family=Great+Vibes&family=Cinzel:wght@400&family=Nunito+Sans:ital,wght@0,300;0,400;1,300&display=swap">
<style>
  :root {
    --page-bg: #f3efe8;
    --card-white: #ffffff;
    --gold: #c9a227;
    --gold-light: #e8c94a;
    --gold-deep: #b08a1c;
    --sky-blue: #a9b6e0;
    --sky-peach: #f7cf9a;
    --sky-yellow: #fbe88e;
    --brick: #b8623e;
    --foliage: #5e7a4a;
    --paving: #d9c4a4;
  }
  * { box-sizing: border-box; margin: 0; padding: 0; }
  html, body { width: 1200px; height: 1200px; overflow: hidden; }
  body {
    background: var(--page-bg);
    position: relative;
    font-family: "Nunito Sans", sans-serif;
    color: var(--gold);
  }
  .spread {
    position: absolute;
    top: 338px;
    left: 30px;
    display: flex;
    gap: 15px;
  }
  .page {
    position: relative;
    width: 370px;
    height: 524px;
    background: var(--card-white);
    box-shadow: 0 2px 10px rgba(0,0,0,0.08);
    overflow: hidden;
  }
  .gold-frame {
    position: absolute;
    inset: 12px;
    border: 2px solid var(--gold);
    pointer-events: none;
    z-index: 3;
  }
  .script { font-family: "Great Vibes", cursive; font-weight: 400; }
  .caps { font-family: "Cinzel", serif; font-weight: 400; }

  /* Page 1 — sky names page */
  .sky-art {
    position: absolute; inset: 0;
    background: linear-gradient(180deg,
      var(--sky-blue) 0%, var(--sky-peach) 18%, var(--sky-yellow) 34%,
      var(--sky-blue) 48%, var(--sky-peach) 60%, var(--sky-yellow) 70%,
      var(--sky-blue) 80%, #b7c3e6 100%);
  }
  .names-stack {
    position: absolute; inset: 0; z-index: 2;
    color: var(--gold-light);
    text-shadow: 0 1px 1px rgba(150,110,20,0.35);
    white-space: nowrap;
  }
  .names-stack .first { position: absolute; top: 140px; left: 50px; font-size: 88px; line-height: 1.2; }
  .names-stack .amp { position: absolute; top: 232px; left: 140px; font-size: 72px; line-height: 1.2; }
  .names-stack .second { position: absolute; top: 312px; left: 150px; font-size: 88px; line-height: 1.2; }

  /* Page 2 — inside details */
  .details {
    position: absolute; inset: 0; z-index: 2;
    text-align: center;
    padding: 56px 30px 0;
  }
  .details .intro { font-size: 14px; line-height: 1.5; font-weight: 400; }
  .details .couple { font-size: 36px; margin-top: 18px; letter-spacing: 1px; line-height: 1.05; }
  .details .and { font-size: 19px; margin: 16px 0 0; line-height: 1.2; }
  .details .when { font-size: 12px; line-height: 1.6; margin-top: 24px; }
  .details .verse {
    font-size: 10.5px; font-style: italic; font-weight: 300;
    line-height: 1.45; margin-top: 34px;
  }

  /* Page 3 — front cover */
  .cover-art {
    position: absolute; top: 14px; left: 14px; right: 14px; bottom: 14px;
    background: linear-gradient(180deg,
      var(--sky-blue) 0%, var(--sky-yellow) 20%, var(--sky-peach) 30%,
      var(--foliage) 40%, var(--brick) 52%, var(--brick) 72%,
      var(--paving) 82%, var(--paving) 100%);
  }
  .cover-text {
    position: absolute; inset: 0; z-index: 2; text-align: center;
    color: var(--gold-light);
    text-shadow: 0 1px 1px rgba(120,85,10,0.45);
  }
  .cover-text .title { font-size: 46px; margin-top: 40px; line-height: 1.1; }
  .cover-text .couple { font-size: 50px; line-height: 1.1; }
  .cover-text .request {
    position: absolute; left: 20px; right: 20px; top: 418px;
    font-size: 12px; white-space: nowrap;
  }
  .cover-text .occasion {
    position: absolute; left: 20px; right: 20px; top: 440px;
    font-size: 30px; letter-spacing: 1px; line-height: 1.2;
  }
</style>
</head>
<body>
  <main class="spread">
    <section class="page page--names">
      <div class="sky-art" role="img" aria-label="Painted sunset sky in soft blue, peach and yellow"></div>
      <div class="names-stack script">
        <span class="first">Polly</span>
        <span class="amp">&amp;</span>
        <span class="second">Ned</span>
      </div>
      <div class="gold-frame"></div>
    </section>

    <section class="page page--details">
      <div class="details">
        <p class="intro">Together with our families<br>You are invited to the Wedding Reception of</p>
        <h1 class="couple caps">Polly Faraway</h1>
        <p class="and caps">and</p>
        <h1 class="couple caps">Ned Bramwick</h1>
        <p class="when">
          On Saturday 9th of September 2017 at 6pm<br>
          At Bramwick's Keep, 41b, Fennow Crescent, Camberley, Surrey, GU19 7QX<br>
          Carriages at 1am<br>
          RSVP by Friday 27th of July to 07712 958 061
        </p>
        <p class="verse">
          With all that we have, we've been truly blessed.<br>
          Your presence and prayers are all that we request.<br>
          But if you desire to give nonetheless,<br>
          Monetary gift is one we suggest.
        </p>
      </div>
      <div class="gold-frame"></div>
    </section>

    <section class="page page--cover">
      <div class="cover-art" role="img" aria-label="Brightened painted illustration of the red-brick family house with lawn, trees, a dog on the grass and a paved driveway under a sunset sky"></div>
      <div class="cover-text">
        <p class="title script">Invitation</p>
        <p class="couple script">Polly &amp; Ned</p>
        <p class="request">Request the pleasure of your company to celebrate their</p>
        <p class="occasion caps">Wedding</p>
      </div>
      <div class="gold-frame"></div>
    </section>
  </main>
</body>
</html>
```